Website for software company "velbra"

We need a website for our software company/startup named "velbra". We are developing several products (currently 3 standard-software products) which are all in different sectors, but all our products are available for Laptops/PC/Mobile Phones/Tablets, ... We do also create custom software and support our customers with consulting to optimize their processes.
We already have a Logo which you can find in the attached files.
We are a young team of 4 members (two founders and 2 employees).

To get an idea of our products -> the first one is a planning software for healthcare organizations (eg. Mercyway, firebrigade, pharmacy), the second one is a booking software for sport clubs and the third one is a competition software for sports hunting. You see very diverse. Include or ignore this info of our products as you like.

The design has to be a bootstrap 4 (or higher) design. We have licenced FontAwesome as iconset. Responsive design should come without saying.

Coding

Coded - Design and coding required

Number of Pages Required

5+ page

Font styles to use
Sans Serif

Requirements
Must have
• Starting page, product pages, news section, contact, team, services

```html
<!DOCTYPE html>
<html lang="en">
<head>
<meta charset="utf-8">
<title>velbra – Software</title>
<link href="https://fonts.googleapis.com/css2?family=Raleway:wght@400;500;600;700;800&family=Open+Sans:wght@400;600&display=swap" rel="stylesheet">
<style>
:root{
  --orange:#f07f1e;
  --orange-dark:#d96a0c;
  --navy:#222c38;
  --navy-2:#2b3542;
  --navy-3:#344050;
  --ink:#1d232b;
  --muted:#6b7480;
  --light:#f4f5f7;
  --white:#ffffff;
}
*{box-sizing:border-box;margin:0;padding:0}
html,body{width:1200px;height:3800px;overflow:hidden}
body{font-family:"Open Sans",Arial,sans-serif;color:var(--ink);background:var(--white);font-size:13px;line-height:1.6}
h1,h2,h3,h4,.brand,.btn,.nav a{font-family:"Raleway",Arial,sans-serif}
.wrap{width:1000px;margin:0 auto;position:relative}
.btn{display:inline-block;background:var(--orange);color:var(--white);font-size:10px;font-weight:700;letter-spacing:.5px;text-transform:uppercase;padding:8px 18px;border-radius:2px}
.fill{display:block}

/* top bar */
.topbar{height:30px;background:var(--navy);color:#cfd5dc;font-size:11px}
.topbar .wrap{display:flex;justify-content:space-between;align-items:center;height:30px}
.social-mini{display:flex;gap:8px}
.social-mini span{width:12px;height:12px;background:#5d6875;border-radius:2px}
.contact-mini{display:flex;gap:20px;align-items:center}
.contact-mini span{display:flex;align-items:center;gap:6px}

/* nav */
.navbar{height:50px;background:var(--white);box-shadow:0 1px 6px rgba(0,0,0,.06);position:relative;z-index:2}
.navbar .wrap{display:flex;justify-content:space-between;align-items:center;height:50px}
.brand{display:flex;align-items:center;gap:8px;font-weight:800;font-size:24px;letter-spacing:1px;color:var(--ink);text-transform:uppercase}
.brand i{width:12px;height:12px;background:var(--orange);display:block}
.nav{display:flex;gap:30px}
.nav a{font-size:11px;font-weight:700;color:var(--ink);text-decoration:none;text-transform:uppercase;letter-spacing:.5px}
.nav a.active{color:var(--orange);border-bottom:2px solid var(--orange);padding-bottom:3px}

/* hero */
.hero{height:400px;position:relative;background:var(--white);overflow:hidden}
.hero-photo{position:absolute;right:0;top:0;width:760px;height:400px;background:linear-gradient(120deg,#e9ecef 0%,#b9b3a8 35%,#5a5f66 70%,#2e3238 100%);clip-path:polygon(14% 0,100% 0,100% 100%,0 100%)}
.hero-text{position:absolute;left:100px;top:90px;width:420px}
.hero-text .lead{font-family:"Raleway",sans-serif;font-size:22px;font-weight:600}
.hero-text h1{font-size:36px;line-height:1.15;font-weight:800;text-transform:uppercase;margin:2px 0 14px}
.hero-text h1 em{font-style:normal;color:var(--orange)}
.hero-text p{font-size:11px;color:var(--muted);width:260px;margin-bottom:18px}

/* welcome */
.welcome{height:420px;position:relative}
.welcome .wrap{display:flex;align-items:center;gap:110px;padding-top:70px;padding-left:30px}
.welcome-art{width:390px;height:280px;background:linear-gradient(135deg,#c9661d,#e9a066 50%,#4a3a30)}
.welcome-text{width:380px}
.welcome-text .kicker{font-family:"Raleway",sans-serif;font-size:14px;font-weight:600}
.welcome-text h2{font-size:32px;font-weight:800;letter-spacing:1px;margin-bottom:12px;color:var(--ink)}
.welcome-text p{font-size:11px;color:var(--muted);margin-bottom:22px}

/* services */
.services{height:480px;background:var(--navy);clip-path:polygon(0 14%,100% 0,100% 100%,0 100%);color:var(--white);padding-top:115px;text-align:center}
.section-head .kicker{font-family:"Raleway",sans-serif;font-size:14px;font-weight:500}
.section-head h2{font-size:32px;font-weight:800;text-transform:uppercase;letter-spacing:1px;margin-bottom:34px}
.section-head h2 em{font-style:normal;color:var(--orange)}
.service-grid{display:flex;gap:20px;justify-content:center;text-align:left}
.service-card{width:310px;height:190px;background:var(--navy-2);display:flex;padding:20px 16px;gap:16px}
.service-num{width:70px;height:110px;flex:none;background:linear-gradient(160deg,#e89a55,#8a4a22)}
.service-card h3{font-size:17px;font-weight:700;line-height:1.25;margin-bottom:8px}
.service-card p{font-size:10px;color:#b8c0ca;margin-bottom:12px;line-height:1.5}
.service-card a{font-size:10px;color:var(--orange);font-weight:700;text-decoration:none}

/* products */
.products{height:500px;text-align:center;padding-top:50px}
.products .section-head h2{color:var(--ink)}
.product-grid{display:flex;justify-content:center;gap:70px}
.product{width:260px}
.product .screen{width:250px;height:150px;margin:0 auto 18px;border-radius:6px 6px 0 0;background:linear-gradient(180deg,#3b4350 0 8px,#eef1f5 8px)}
.product .screen.red{background:linear-gradient(180deg,#3b4350 0 8px,#fbe8e8 8px,#ffffff)}
.product .screen.cream{background:linear-gradient(180deg,#3b4350 0 8px,#f6efe4 8px)}
.product .base{width:280px;height:8px;margin:-18px auto 18px;background:#b9bec6;border-radius:0 0 6px 6px}
.product h3{font-size:14px;font-weight:600;margin-bottom:4px}
.product p{font-size:10px;color:var(--muted);margin:0 auto 14px;width:200px;line-height:1.5}

/* news */
.news{height:500px;background:linear-gradient(135deg,#1c252f,#2b3542);clip-path:polygon(0 0,100% 6%,100% 94%,0 100%);color:var(--white);text-align:center;padding-top:70px}
.news-grid{display:flex;justify-content:center;gap:50px;text-align:left}
.news-card{width:250px}
.news-card .photo{height:160px;margin-bottom:12px;background:linear-gradient(135deg,#8e9aa8,#4a5563)}
.news-card .photo.b{background:linear-gradient(135deg,#c9cfd6,#5e6a78)}
.news-card .photo.c{background:linear-gradient(135deg,#a9c2d6,#4b6378)}
.news-card .date{font-size:9px;color:var(--orange);font-weight:600}
.news-card h3{font-size:16px;font-weight:600;line-height:1.25;margin:4px 0 12px}

/* team */
.team{height:470px;text-align:center;padding-top:60px}
.team .section-head h2{color:var(--ink)}
.team-grid{display:flex;justify-content:center;gap:18px}
.member{width:220px}
.member .photo{height:230px;background:linear-gradient(160deg,#c49a7e,#6e5446);margin-bottom:10px}
.member .photo.b{background:linear-gradient(160deg,#d8d2c9,#7a6a5a)}
.member .photo.c{background:linear-gradient(160deg,#bfc6cd,#6a5a52)}
.member .photo.d{background:linear-gradient(160deg,#a38a78,#3e3630)}
.member h4{font-size:14px;font-weight:600}
.member span{font-size:10px;color:var(--muted)}

/* contact */
.contact{height:480px;background:var(--navy);clip-path:polygon(0 0,100% 16%,100% 100%,0 100%);color:var(--white);text-align:center;padding-top:110px}
.contact-form{width:700px;margin:0 auto;display:grid;grid-template-columns:1fr 1fr;gap:10px 10px;text-align:left}
.field{background:var(--white);color:#8a929c;font-size:11px;padding:8px 12px;height:34px}
.field.msg{grid-row:span 3;height:122px}
.submit{grid-column:span 2;background:var(--orange);color:var(--white);text-align:center;font-family:"Raleway",sans-serif;font-weight:700;font-size:11px;padding:9px;text-transform:uppercase}

/* footer */
.footer{height:430px;background:#141a21;color:#aab3bd;padding-top:70px}
.footer .wrap{display:flex;gap:60px}
.footer-about{width:280px}
.footer-about .brand{color:var(--white);font-size:30px;margin-bottom:14px}
.footer-about p{font-size:11px;margin-bottom:16px}
.socials{display:flex;gap:8px}
.socials span{width:22px;height:22px;background:var(--navy-3);display:block}
.footer-col h4{color:var(--orange);font-size:14px;font-weight:700;margin-bottom:12px}
.footer-col ul{list-style:none;font-size:11px}
.footer-col li{margin-bottom:6px;display:flex;align-items:flex-start;gap:8px}
.footer-col.contact-col{width:230px}
.copyright{height:40px;background:#0e1217;color:#7d8590;font-size:10px;text-align:center;line-height:40px}
.copyright b{color:var(--orange);font-weight:600}
</style>
</head>
<body>

<header>
  <div class="topbar">
    <div class="wrap">
      <div class="social-mini"><span></span><span></span><span></span></div>
      <div class="contact-mini">
        <span><svg width="10" height="10" viewBox="0 0 24 24"><path fill="#f07f1e" d="M6.6 10.8a15 15 0 006.6 6.6l2.2-2.2a1 1 0 011-.25 11.4 11.4 0 003.6.6 1 1 0 011 1V20a1 1 0 01-1 1A17 17 0 013 4a1 1 0 011-1h3.5a1 1 0 011 1c0 1.25.2 2.45.6 3.6a1 1 0 01-.25 1z"/></svg>+01 234 567 890</span>
        <span><svg width="11" height="9" viewBox="0 0 24 18"><rect x="1" y="1" width="22" height="16" fill="none" stroke="#f07f1e" stroke-width="2"/><path d="M1 1l11 9 11-9" fill="none" stroke="#f07f1e" stroke-width="2"/></svg>hello@velbra.io</span>
      </div>
    </div>
  </div>
  <nav class="navbar">
    <div class="wrap">
      <div class="brand"><i></i>velbra</div>
      <div class="nav">
        <a class="active" href="#">Home</a><a href="#">Services</a><a href="#">Products</a><a href="#">News</a><a href="#">Team</a><a href="#">Contact Us</a>
      </div>
    </div>
  </nav>
</header>

<section class="hero">
  <div class="hero-photo fill" role="img" aria-label="Photo of two business people talking on a sofa in a bright office"></div>
  <div class="hero-text">
    <div class="lead">Organize</div>
    <h1>Your <em>Projects</em><br>easier than before</h1>
    <p>Plan every task in one place, keep your team aligned and deliver faster.</p>
    <span class="btn">Read more</span>
  </div>
</section>

<section class="welcome">
  <div class="wrap">
    <div class="welcome-art fill" role="img" aria-label="Collage of office team photos in warm orange tones"></div>
    <div class="welcome-text">
      <div class="kicker">Welcome To</div>
      <h2>VELBRA</h2>
      <p>We are a young software team building products for healthcare, sport clubs and sports hunting. Our tools run on laptops, desktops, tablets and phones alike. Beyond our own products we create custom software and consult our clients to make their daily processes simpler, faster and more reliable.</p>
      <span class="btn">Read more</span>
    </div>
  </div>
</section>

<section class="services">
  <div class="section-head">
    <div class="kicker">How we do</div>
    <h2><em>Our</em> Services</h2>
  </div>
  <div class="service-grid">
    <div class="service-card">
      <div class="service-num fill" role="img" aria-label="Office photo for service one"></div>
      <div><h3>Efficient Database Security</h3><p>Your data stays safe with encrypted storage, backups and access rules built in.</p><a href="#">Read More</a></div>
    </div>
    <div class="service-card">
      <div class="service-num fill" role="img" aria-label="Office photo for service two"></div>
      <div><h3>Achieve Global Development</h3><p>Scalable software that grows with your organisation across regions and devices.</p><a href="#">Read More</a></div>
    </div>
    <div class="service-card">
      <div class="service-num fill" role="img" aria-label="Office photo for service three"></div>
      <div><h3>Analytical Solutions System</h3><p>Clear reports and dashboards that turn your daily data into better decisions.</p><a href="#">Read More</a></div>
    </div>
  </div>
</section>

<section class="products">
  <div class="section-head">
    <div class="kicker">Featured</div>
    <h2><em>Several</em> Products</h2>
  </div>
  <div class="product-grid">
    <div class="product">
      <div class="screen fill" role="img" aria-label="Laptop showing a healthcare planning dashboard"></div><div class="base"></div>
      <h3>Healthcare Organizations</h3><p>Shift and resource planning for clinics, rescue services and pharmacies.</p><span class="btn">Read more</span>
    </div>
    <div class="product">
      <div class="screen red fill" role="img" aria-label="Laptop showing a sport club booking dashboard"></div><div class="base"></div>
      <h3>Sport Clubs</h3><p>Book courts, courses and members in a few clicks on any device.</p><span class="btn">Read more</span>
    </div>
    <div class="product">
      <div class="screen cream fill" role="img" aria-label="Laptop showing a sports hunting competition dashboard"></div><div class="base"></div>
      <h3>Sports Hunting</h3><p>Run competitions, scores and rankings with live result tracking.</p><span class="btn">Read more</span>
    </div>
  </div>
</section>

<section class="news">
  <div class="section-head">
    <div class="kicker">Recent Post</div>
    <h2><em>Latest</em> News</h2>
  </div>
  <div class="news-grid">
    <div class="news-card">
      <div class="photo fill" role="img" aria-label="Photo of a team meeting around a table"></div>
      <div class="date">12 MARCH, 2024</div>
      <h3>At vero eos et accusamus et iusto odio dignissimos</h3>
      <span class="btn">Read more</span>
    </div>
    <div class="news-card">
      <div class="photo b fill" role="img" aria-label="Photo of two colleagues talking in an office"></div>
      <div class="date">28 FEBRUARY, 2024</div>
      <h3>At vero eos et accusamus et iusto odio dignissimos</h3>
      <span class="btn">Read more</span>
    </div>
    <div class="news-card">
      <div class="photo c fill" role="img" aria-label="Photo of a businesswoman in front of glass buildings"></div>
      <div class="date">14 FEBRUARY, 2024</div>
      <h3>At vero eos et accusamus et iusto odio dignissimos</h3>
      <span class="btn">Read more</span>
    </div>
  </div>
</section>

<section class="team">
  <div class="section-head">
    <div class="kicker">Members</div>
    <h2><em>Our</em> Team</h2>
  </div>
  <div class="team-grid">
    <div class="member"><div class="photo fill" role="img" aria-label="Portrait photo of a founder"></div><h4>Arlo Gennick</h4><span>Founder</span></div>
    <div class="member"><div class="photo b fill" role="img" aria-label="Portrait photo of a founder"></div><h4>Wendel Patroni</h4><span>Founder</span></div>
    <div class="member"><div class="photo c fill" role="img" aria-label="Portrait photo of an employee"></div><h4>Sina Pradell</h4><span>Employee</span></div>
    <div class="member"><div class="photo d fill" role="img" aria-label="Portrait photo of an employee"></div><h4>Dario Ruelas</h4><span>Employee</span></div>
  </div>
</section>

<section class="contact">
  <div class="section-head">
    <div class="kicker">Contact</div>
    <h2><em>Quick</em> Contact</h2>
  </div>
  <form class="contact-form">
    <div class="field">Name</div>
    <div class="field msg">Message</div>
    <div class="field">Email</div>
    <div class="field">Phone</div>
    <div class="submit">Submit</div>
  </form>
</section>

<footer>
  <div class="footer">
    <div class="wrap">
      <div class="footer-about">
        <div class="brand">velbra</div>
        <p>We build reliable software for healthcare, sport clubs and sports hunting, and help our clients optimise their processes.</p>
        <div class="socials"><span></span><span></span><span></span></div>
      </div>
      <div class="footer-col">
        <h4>Sitemap</h4>
        <ul><li>› Home</li><li>› Services</li><li>› Products</li><li>› News</li><li>› Team</li><li>› Contact Us</li></ul>
      </div>
      <div class="footer-col">
        <h4>Products</h4>
        <ul><li>› Healthcare Organizations</li><li>› Sport Clubs</li><li>› Sports Hunting</li></ul>
      </div>
      <div class="footer-col contact-col">
        <h4>Contact Us</h4>
        <ul>
          <li><svg width="12" height="14" viewBox="0 0 24 28"><path fill="#f07f1e" d="M12 0a10 10 0 00-10 10c0 8 10 18 10 18s10-10 10-18A10 10 0 0012 0zm0 14a4 4 0 110-8 4 4 0 010 8z"/></svg>42 Larkfield Lane, 4021 Brightwater</li>
          <li><svg width="12" height="12" viewBox="0 0 24 24"><path fill="#f07f1e" d="M6.6 10.8a15 15 0 006.6 6.6l2.2-2.2a1 1 0 011-.25 11.4 11.4 0 003.6.6 1 1 0 011 1V20a1 1 0 01-1 1A17 17 0 013 4a1 1 0 011-1h3.5a1 1 0 011 1c0 1.25.2 2.45.6 3.6a1 1 0 01-.25 1z"/></svg>+01 234 567 890</li>
          <li><svg width="12" height="10" viewBox="0 0 24 18"><rect x="1" y="1" width="22" height="16" fill="none" stroke="#f07f1e" stroke-width="2"/><path d="M1 1l11 9 11-9" fill="none" stroke="#f07f1e" stroke-width="2"/></svg>hello@velbra.io</li>
        </ul>
      </div>
    </div>
  </div>
  <div class="copyright">Copyright © 2024 <b>velbra</b>. All Rights Reserved.</div>
</footer>

</body>
</html>
```